Brambury Logistics

Create a modern, simple, Elegant business card design for my business.

Services: Tamo Trucks, Transport, Contract Logistics,

Industry/Entity Type

Business

Contact Information for Business Card

Include all details same as old card plus new website address: www.bramburylogistics.com.au

Requirements
Must have
• Similar colors to Logo.

```html
<!DOCTYPE html>
<html lang="en">
<head>
<meta charset="utf-8">
<title>Brambury Logistics – Business Card</title>
<link rel="stylesheet" href="https://fonts.googleapis.com/css2?family=Open+Sans:wght@400;600;700&display=swap">
<style>
  :root {
    --backdrop: #86989a;
    --card-black: #070808;
    --card-dark: #141617;
    --panel-grey: #aebbba;
    --text-white: #f4f6f6;
    --brand-silver: #c9cfd2;
    --brand-blue: #2f6fc0;
    --rule: #4a4d4f;
  }
  * { margin: 0; padding: 0; box-sizing: border-box; }
  html, body { width: 1200px; height: 600px; overflow: hidden; }
  body {
    background: var(--backdrop);
    font-family: "Open Sans", sans-serif;
    position: relative;
  }
  .card {
    position: absolute;
    top: 178px;
    width: 502px;
    height: 290px;
    overflow: hidden;
  }
  .card-front { left: 76px; }
  .card-back { left: 646px; }

  .texture {
    position: absolute;
    inset: 0;
    background:
      radial-gradient(ellipse at 85% 10%, #2a2d2f 0%, transparent 45%),
      radial-gradient(ellipse at 90% 80%, #232628 0%, transparent 50%),
      linear-gradient(160deg, var(--card-dark) 0%, var(--card-black) 60%);
  }

  .front-name {
    position: absolute;
    left: 0; right: 0;
    top: 124px;
    text-align: center;
    font-size: 34px;
    font-weight: 700;
    color: var(--brand-silver);
    letter-spacing: 0.5px;
  }

  .contact-side {
    position: absolute;
    left: 0; top: 0;
    width: 318px; height: 290px;
  }
  .contact-row {
    position: absolute;
    left: 18px;
    display: flex;
    align-items: center;
    color: var(--text-white);
  }
  .contact-row svg { flex: none; }
  .row-name { top: 17px; }
  .row-name .label { font-size: 21px; margin-left: 14px; }
  .row-phone { top: 78px; }
  .row-phone .label { font-size: 20px; margin-left: 16px; letter-spacing: 0.5px; }
  .row-email { top: 144px; }
  .row-email .label { font-size: 12.5px; margin-left: 14px; }
  .row-web { top: 198px; }
  .row-web .label { font-size: 12.5px; margin-left: 18px; }
  .rule {
    position: absolute;
    left: 0; top: 250px;
    width: 318px; height: 1px;
    background: var(--rule);
  }

  .brand-panel {
    position: absolute;
    left: 318px; top: 0;
    width: 184px; height: 290px;
    background: var(--panel-grey);
  }
  .panel-name {
    position: absolute;
    left: 0; right: 0;
    top: 118px;
    text-align: center;
    font-size: 16px;
    font-weight: 700;
    color: var(--brand-blue);
  }
</style>
</head>
<body>
  <section class="card card-front">
    <div class="texture"></div>
    <div class="front-name">Brambury Logistics</div>
  </section>

  <section class="card card-back">
    <div class="texture"></div>
    <div class="contact-side">
      <div class="contact-row row-name">
        <svg width="36" height="36" viewBox="0 0 36 36" aria-hidden="true">
          <circle cx="18" cy="18" r="18" fill="#fff"/>
          <circle cx="18" cy="14" r="5" fill="#070808"/>
          <path d="M9 27 q9 -12 18 0 z" fill="#070808"/>
        </svg>
        <span class="label">Name &amp; Surname</span>
      </div>
      <div class="contact-row row-phone">
        <svg width="36" height="36" viewBox="0 0 24 24" aria-hidden="true">
          <path fill="#fff" d="M6.6 10.8a15.1 15.1 0 0 0 6.6 6.6l2.2-2.2a1 1 0 0 1 1-.25 11.4 11.4 0 0 0 3.6.57 1 1 0 0 1 1 1V20a1 1 0 0 1-1 1A17 17 0 0 1 3 4a1 1 0 0 1 1-1h3.5a1 1 0 0 1 1 1c0 1.25.2 2.45.57 3.57a1 1 0 0 1-.25 1z"/>
        </svg>
        <span class="label">0412 555 038</span>
      </div>
      <div class="contact-row row-email">
        <svg width="38" height="36" viewBox="0 0 38 36" aria-hidden="true">
          <path d="M2 14 L19 2 L36 14 V34 H2 Z" fill="none" stroke="#fff" stroke-width="1.6"/>
          <path d="M2 14 L19 26 L36 14 M2 34 L15 23 M36 34 L23 23" fill="none" stroke="#fff" stroke-width="1.6"/>
          <text x="19" y="17" text-anchor="middle" font-size="11" font-weight="700" fill="#fff" font-family="Open Sans, sans-serif">@</text>
        </svg>
        <span class="label">Kiran@bramburylogistics.com.au</span>
      </div>
      <div class="contact-row row-web">
        <svg width="34" height="34" viewBox="0 0 34 34" aria-hidden="true">
          <g fill="none" stroke="#fff" stroke-width="1.4">
            <circle cx="17" cy="17" r="15"/>
            <ellipse cx="17" cy="17" rx="7" ry="15"/>
            <line x1="17" y1="2" x2="17" y2="32"/>
            <line x1="2" y1="17" x2="32" y2="17"/>
            <path d="M5 9 H29 M5 25 H29"/>
          </g>
        </svg>
        <span class="label">www.bramburylogistics.com.au</span>
      </div>
      <div class="rule"></div>
    </div>
    <div class="brand-panel">
      <div class="panel-name">Brambury Logistics</div>
    </div>
  </section>
</body>
</html>
```